Brivane - Business Cards for a new venture

create business card for a startup classified business dealing in construction materials, the cards need to have a professional look but modern, more serious than playful, one of the samples must include the official font (attached), please explore using the official colors in the company's logo

Target Market(s)

Energy sector

Contact Information for Business Card

Font styles to use
Other font styles liked:
• suissnord

Requirements
Must have
• corporate colors (in logo attached)
Nice to have
• Official font (in one of the samples) font is : suissnord
Should not have
• Cartoonish look

```html
<!DOCTYPE html>
<html lang="en">
<head>
<meta charset="utf-8">
<title>Brivane Business Cards</title>
<link href="https://fonts.googleapis.com/css2?family=Open+Sans:wght@400;600&display=swap" rel="stylesheet">
<style>
  :root {
    --brand-blue: #164579;
    --ink-blue: #1b4a85;
    --ink-grey: #5f5f5f;
    --mark-grey: #8e8e8e;
    --card-white: #ffffff;
    --backdrop: #555555;
  }
  * { margin: 0; padding: 0; box-sizing: border-box; }
  html, body {
    width: 1200px; height: 1000px; overflow: hidden;
    background: var(--backdrop);
    font-family: "Open Sans", Arial, sans-serif;
  }
  .stage { position: relative; width: 1200px; height: 1000px; }
  .card {
    position: absolute; left: 267px; width: 666px; height: 396px;
    box-shadow: 0 2px 8px rgba(0,0,0,0.35);
  }
  .card-front { top: 76px; background: var(--brand-blue); }
  .card-back { top: 535px; background: var(--card-white); }

  .front-name {
    position: absolute; left: 0; right: 0; top: 250px;
    text-align: center; color: var(--card-white);
    font-size: 40px; font-weight: 400; letter-spacing: 6px;
  }
  .front-dot {
    position: absolute; left: 303px; top: 120px;
    width: 60px; height: 60px; border-radius: 50%;
    background: var(--card-white);
  }

  .back-dot {
    position: absolute; left: 448px; top: 70px;
    width: 44px; height: 44px; border-radius: 50%;
    background: var(--ink-blue);
  }
  .back-name {
    position: absolute; left: 345px; width: 250px; top: 154px;
    text-align: center; color: var(--mark-grey);
    font-size: 28px; font-weight: 400; letter-spacing: 4px;
  }

  .holder { position: absolute; left: 48px; top: 228px; }
  .holder-name { color: var(--ink-blue); font-size: 23px; font-weight: 600; line-height: 1.2; }
  .holder-role { color: var(--ink-grey); font-size: 16px; line-height: 1.2; }
  .divider {
    position: absolute; left: 50px; top: 292px;
    width: 48px; height: 4px; background: var(--ink-blue);
  }
  .contact {
    position: absolute; left: 50px; color: var(--ink-grey);
    font-size: 15.5px; white-space: nowrap;
  }
  .contact-phones { top: 315px; }
  .contact-address { top: 344px; letter-spacing: 0.4px; }
  .contact b { color: var(--ink-blue); font-weight: 600; }
  .sep { margin: 0 8px; }
</style>
</head>
<body>
<main class="stage">
  <section class="card card-front">
    <span class="front-dot"></span>
    <div class="front-name">BRIVANE</div>
  </section>

  <section class="card card-back">
    <span class="back-dot"></span>
    <div class="back-name">BRIVANE</div>

    <div class="holder">
      <div class="holder-name">Elena Marchetti</div>
      <div class="holder-role">Founder / Consultant</div>
    </div>
    <div class="divider"></div>

    <div class="contact contact-phones">
      <b>M:</b> + 999 999 9999<span class="sep">|</span><b>P:</b> + 999 999 9999<span class="sep">|</span><b>E:</b> elena@brivane.com
    </div>
    <div class="contact contact-address">
      <b>A:</b> 3170 Larkfield Ave. Suite 4, Nashville, TN 37204
    </div>
  </section>
</main>
</body>
</html>
```